Stationery Design Project for Marketing Consultancy

I have started a new consultancy business and require the following elements to be designed using existing logo:
• Business card
• Letterhead
• Envelope (DL, C4, C5)
• Microsoft word template for report writing
• A4 Presentation Folder
• Powerpoint template
COPY FOR FRONT AND BACK OF BUSINESS CARD
logo
'Countable Growth. Bold Outcomes' slogan (but no need to use existing lockup with logo)
name, B Bus. Mktg, Grad Dip Digital Mktg, CPM (post nominal abbreviations in smaller font)
mobile: 04XX-XXX-XXX (I will give details to the winner to add)
website: www.quorvale.com.au
email: info@quorvale.com.au
COPY FOR LETTERHEAD
Logo
Company Name
Please, submit your designs that include business card, letterhead and envelope. Once selected the winner will be asked to complete the project by creating the rest of the artwork.
FINAL FILES
Print ready files to be supplied as well as Indesign files so that minor amends can be made if necessary in future.
• Layered vectors in EPS & PDF
• Screen quality JPEG & PNGs
ABOUT THE BUSINESS: QUORVALE
I work with clients to understand their business challenges, developing and executing measurable marketing strategies tied to key business metrics. Services include:
Services include:
• Business planning and business development
• Marketing and brand strategy
• Insight-driven integrated campaigns
• Loyalty programs and retention marketing
• Marketing automation
• Direct marketing (traditional and digital)
• Content strategy and development
Hi everyone,
Target Market(s)
Corporate decision makers (heads of marketing, general managers etc) and small to medium sized business owners. Predominately male aged 35+
Industry/Entity Type
Marketing
Requirements
Must have
- BRAND PERSONALITY
The successful design will communicate brand personality. I am a professional, results-driven entrepreneur, but want to show off my creative flair.
MEMORABILITY
Looking for a unique and eye-catching design. Am considering special printing effects (die cuts, letterpress, interactive elements, embossing, foiling etc) or a striking minimalist approach.
Nice to have
- I have a mission that could be incorporated on reverse if room -
Turning insights into actions & passion into profit.
Should not have
- Use of pink or green.

```html
<!DOCTYPE html>
<html lang="en">
<head>
<meta charset="utf-8">
<title>Quorvale Business Card</title>
<link href="https://fonts.googleapis.com/css2?family=Open+Sans:wght@400;700&family=Questrial&display=swap" rel="stylesheet">
<style>
  :root {
    --bg: #4a4b4d;
    --card-white-a: #f4f4f4;
    --card-white-b: #d9d9d9;
    --brand-blue: #1a6a9c;
    --brand-blue-deep: #0e4a78;
    --brand-blue-light: #1f86c2;
    --ink-blue: #1b5f8e;
    --wordmark-grey: #c9c9c9;
    --white: #ffffff;
    --list-ink: #e4eef6;
  }
  * { box-sizing: border-box; margin: 0; padding: 0; }
  html, body { width: 1200px; height: 1000px; overflow: hidden; }
  body { background: var(--bg); position: relative; font-family: "Questrial", sans-serif; }

  .card {
    position: absolute;
    top: 349px;
    width: 528px;
    height: 301px;
    border-radius: 16px;
    overflow: hidden;
  }

  /* Front */
  .card-front {
    left: 68px;
    background: linear-gradient(120deg, var(--card-white-a) 0%, #ebebeb 55%, var(--card-white-b) 100%);
  }
  .front-sheen {
    position: absolute; left: 300px; top: 0; width: 228px; height: 301px;
    background: radial-gradient(ellipse at 60% 50%, rgba(190,190,190,0.45), rgba(190,190,190,0) 70%);
  }
  .holder-name {
    position: absolute; left: 27px; top: 26px;
    font-family: "Open Sans", sans-serif; font-weight: 700;
    font-size: 15px; letter-spacing: 0.3px; color: var(--ink-blue);
  }
  .holder-title {
    position: absolute; left: 27px; top: 46px;
    font-size: 13px; color: var(--ink-blue);
  }
  .brand-dot {
    position: absolute; left: 30px; top: 104px;
    width: 58px; height: 58px; border-radius: 50%;
    background: var(--brand-blue-light);
  }
  .front-wordmark {
    position: absolute; left: 27px; top: 204px;
    font-family: "Open Sans", sans-serif; font-weight: 700;
    font-size: 21px; letter-spacing: 0.5px; color: var(--wordmark-grey);
  }
  .contact-list { position: absolute; left: 27px; top: 242px; list-style: none; }
  .contact-list li {
    display: flex; align-items: center; gap: 11px;
    font-size: 13.5px; color: var(--ink-blue); height: 20px;
  }
  .contact-list svg { width: 15px; height: 15px; }

  /* Back */
  .card-back {
    left: 612px;
    background: linear-gradient(160deg, var(--brand-blue) 0%, #145b8a 45%, var(--brand-blue-deep) 100%);
  }
  .back-motif {
    position: absolute; left: 0; top: 20px; width: 190px; height: 270px;
    background: radial-gradient(ellipse at 40% 45%, rgba(40,150,210,0.55), rgba(40,150,210,0) 72%);
  }
  .back-wordmark {
    position: absolute; left: 218px; top: 30px;
    font-family: "Open Sans", sans-serif; font-weight: 700;
    font-size: 40px; letter-spacing: 0.5px; color: var(--white);
  }
  .tagline {
    position: absolute; left: 218px; top: 80px;
    font-family: "Open Sans", sans-serif; font-weight: 700;
    font-size: 11px; letter-spacing: 0.2px; color: var(--white); text-transform: uppercase;
  }
  .services {
    position: absolute; left: 218px; top: 119px; list-style: none;
    font-size: 13px; line-height: 15.5px; color: var(--list-ink);
  }
  .services li::before { content: "• "; }
  .website {
    position: absolute; left: 218px; top: 258px;
    display: flex; align-items: center; gap: 11px;
    font-size: 13.5px; color: var(--list-ink);
  }
  .website b { font-family: "Open Sans", sans-serif; font-weight: 700; }
  .website svg { width: 15px; height: 15px; }
</style>
</head>
<body>

<section class="card card-front">
  <div class="front-sheen"></div>
  <h1 class="holder-name">DANIEL HARTLEY</h1>
  <p class="holder-title">Managing Director</p>
  <div class="brand-dot"></div>
  <p class="front-wordmark">QUORVALE</p>
  <ul class="contact-list">
    <li>
      <svg viewBox="0 0 16 16" aria-hidden="true"><circle cx="8" cy="8" r="7" fill="none" stroke="#1b5f8e" stroke-width="1.2"/><rect x="5.8" y="3.8" width="4.4" height="8.4" rx="0.8" fill="none" stroke="#1b5f8e" stroke-width="1.1"/></svg>
      +0491-570-156
    </li>
    <li>
      <svg viewBox="0 0 16 16" aria-hidden="true"><circle cx="8" cy="8" r="7.5" fill="#1b5f8e"/><rect x="4" y="5.3" width="8" height="5.6" fill="#fff"/><path d="M4 5.3 L8 8.5 L12 5.3" fill="none" stroke="#1b5f8e" stroke-width="1"/></svg>
      info@quorvale.com.au
    </li>
  </ul>
</section>

<section class="card card-back">
  <div class="back-motif" role="img" aria-label="Large soft brand decoration area"></div>
  <p class="back-wordmark">QUORVALE</p>
  <p class="tagline">Countable Growth. Bold Outcomes.</p>
  <ul class="services">
    <li>Business planning and business development</li>
    <li>Marketing and brand strategy</li>
    <li>Insight-driven integrated campaigns</li>
    <li>Loyalty programs and retention marketing</li>
    <li>Marketing automation</li>
    <li>Direct marketing (traditional and digital)</li>
    <li>Content strategy and development</li>
  </ul>
  <p class="website">
    <svg viewBox="0 0 16 16" aria-hidden="true" fill="none" stroke="#e4eef6" stroke-width="1"><circle cx="8" cy="8" r="6.5"/><ellipse cx="8" cy="8" rx="2.8" ry="6.5"/><line x1="1.5" y1="8" x2="14.5" y2="8"/><path d="M2.6 4.8 H13.4 M2.6 11.2 H13.4"/></svg>
    <span>www.<b>quorvale</b>.com.au</span>
  </p>
</section>

</body>
</html>
```